Business Card Design

educational services
broker of essential services
So I love my The Copper Kettle cards. I love the background.
I like the background on the harbor crest card
I like a little part of each Meridel card
I want my card to stand out and be professional
I would also like somewhat of a brand
I do not want it to be specific to anything but the world and galaxy
I would like to be able to be used for everything, all encompassing
In spanish Sin fronteras, not sureother languages but i will do programs for other countries like China, Japan and Korea
Reason: It has been the first week of school and I have not been able to get the feedback I need.
Please change colors to Blue and GOld
Please add ~ over the n in Lucia
Please submit some vertical designs
Please include the world
Please make eagle a watermark
Make sure the Open Horizons doesnt have "learning academy" under it
I am open to new designs and I will pay more after I chose a designer who seems to get all this stuff in my head!
Reason: Last minute designs were wonderful
Reason: I was out of town and not able to review the wonderful designs posted. I am narrowing the designs down now! I appreciate all the work done thus far.
Hello,
Thank you for all the designs. This is difficult. I have not been able to access them as I was able to last week so please be patient. If you also do web design please send me a message.
Again, thank you. I am down to just a few designs.
Sincerely,
Lucia Ferrant Dowell
I have been extremely busy, I should pick a design by the ned of this week. Thank you for your patience
Industry/Entity Type
Business
Contact Information for Business Card
Dr. Lucia Ferrant Dowell
www.ohlearn.example
(555) 284-9063 US
luciaannferrant@mailbox.example
Look and feel

```html
<!DOCTYPE html>
<html lang="en">
<head>
<meta charset="utf-8">
<title>Open Horizons – Business Card</title>
<link rel="stylesheet" href="https://fonts.googleapis.com/css2?family=Vollkorn:wght@700&family=EB+Garamond:wght@500&display=swap">
<style>
  :root {
    --page: #ffffff;
    --blue-deep: #1b5690;
    --blue-mid: #4384b8;
    --gold: #f3e21a;
    --gold-dark: #c9b40e;
    --gold-light: #fff6a0;
    --white: #ffffff;
    --sky-top: #dfe3e6;
    --sky-mid: #f1ede4;
    --city: #e6e8ea;
    --logo-gold: #e6d21a;
  }
  * { margin: 0; padding: 0; box-sizing: border-box; }
  html, body {
    width: 1200px; height: 809px; overflow: hidden;
    background: var(--page);
  }
  .card {
    position: absolute; left: 110px; top: 85px;
    width: 1087px; height: 638px; overflow: hidden;
  }
  .card-art { position: absolute; inset: 0; width: 1087px; height: 638px; }
  .name {
    position: absolute; left: 462px; top: 72px;
    font-family: "Vollkorn", Georgia, serif; font-weight: 700;
    font-size: 44px; color: var(--gold); white-space: nowrap;
    letter-spacing: 0.3px;
  }
  .name-rule {
    position: absolute; left: 462px; top: 153px; width: 625px; height: 1px;
    background: rgba(255,255,255,0.8);
  }
  .contact-list {
    position: absolute; left: 593px; top: 182px; list-style: none;
    font-family: "EB Garamond", Georgia, serif; font-weight: 500;
    font-size: 30px; color: var(--white);
  }
  .contact-item { display: flex; align-items: center; height: 40px; }
  .contact-icon {
    width: 22px; height: 22px; margin-right: 16px; flex: none;
  }
  .brand {
    position: absolute; left: 50px; top: 438px;
    display: flex; align-items: center;
  }
  .brand-dot {
    width: 124px; height: 124px; border-radius: 50%;
    background: var(--blue-mid); margin-right: 26px; flex: none;
  }
  .brand-name {
    font-family: "EB Garamond", Georgia, serif; font-weight: 500;
    font-size: 82px; color: var(--logo-gold); white-space: nowrap;
  }
</style>
</head>
<body>
  <div class="card">
    <svg class="card-art" viewBox="0 0 1087 638" xmlns="http://www.w3.org/2000/svg">
      <defs>
        <linearGradient id="photoTone" x1="0" y1="0" x2="0" y2="1">
          <stop offset="0" stop-color="var(--sky-top)"/>
          <stop offset="0.35" stop-color="var(--sky-mid)"/>
          <stop offset="0.6" stop-color="#cfd3d6"/>
          <stop offset="1" stop-color="var(--city)"/>
        </linearGradient>
        <linearGradient id="blueField" x1="0" y1="0" x2="1" y2="0">
          <stop offset="0" stop-color="var(--blue-deep)"/>
          <stop offset="0.4" stop-color="var(--blue-mid)"/>
          <stop offset="1" stop-color="var(--blue-deep)"/>
        </linearGradient>
        <linearGradient id="goldBand" x1="0" y1="0" x2="1" y2="0">
          <stop offset="0" stop-color="var(--gold-dark)"/>
          <stop offset="0.3" stop-color="var(--gold-light)"/>
          <stop offset="0.7" stop-color="var(--gold-dark)"/>
          <stop offset="0.9" stop-color="var(--gold-light)"/>
          <stop offset="1" stop-color="var(--gold-dark)"/>
        </linearGradient>
      </defs>
      <rect class="photo-fill" width="1087" height="638" fill="url(#photoTone)"
            role="img" aria-label="City skyline photograph with a bald eagle in flight"/>
      <path class="gold-swoosh" fill="url(#goldBand)"
            d="M0,220 C50,160 130,125 230,125 C340,125 430,235 560,320 C720,425 900,455 1087,420 V455 C900,490 720,460 560,365 C430,285 340,150 230,148 C130,148 50,185 0,245 Z"/>
      <path class="blue-field" fill="url(#blueField)"
            d="M0,0 H1087 V420 C900,455 720,425 560,320 C430,235 340,125 230,125 C130,125 50,160 0,220 Z"/>
    </svg>

    <h1 class="name">Dr. Lucia Ferrant Dowell</h1>
    <div class="name-rule"></div>

    <ul class="contact-list">
      <li class="contact-item">
        <svg class="contact-icon" viewBox="0 0 22 22"><rect width="22" height="22" rx="4" fill="var(--gold)"/><path d="M6,5 l3,0 1,4 -2,1 c1,2 2,3 4,4 l1,-2 4,1 0,3 c-6,1 -11,-4 -11,-11z" fill="var(--blue-deep)"/></svg>
        (555) 284-9063 US
      </li>
      <li class="contact-item">
        <svg class="contact-icon" viewBox="0 0 22 22"><rect width="22" height="22" rx="4" fill="var(--gold)"/><rect x="4" y="6" width="14" height="10" fill="var(--blue-deep)"/><path d="M4,6 l7,5 7,-5" fill="none" stroke="var(--gold)" stroke-width="1.5"/></svg>
        luciaannferrant@mailbox.example
      </li>
      <li class="contact-item">
        <svg class="contact-icon" viewBox="0 0 22 22"><rect width="22" height="22" rx="4" fill="var(--gold)"/><circle cx="11" cy="11" r="7" fill="none" stroke="var(--blue-deep)" stroke-width="1.5"/><ellipse cx="11" cy="11" rx="3" ry="7" fill="none" stroke="var(--blue-deep)" stroke-width="1.2"/><path d="M4,11 h14" stroke="var(--blue-deep)" stroke-width="1.2"/></svg>
        www.ohlearn.example
      </li>
    </ul>

    <div class="brand">
      <span class="brand-dot"></span>
      <span class="brand-name">Open Horizons</span>
    </div>
  </div>
</body>
</html>
```